Conservative, Modern and Sharp Builder Business card

Hi there,
We would like to update our existing business card.
I have attached photos of existing business card, logo and van sign.

I would like the business card to also list what we do :
Renovation • New Build • Alteration
Extension • Bathroom • Maintenance.(Seperated by dots)

Contact number : 021 0483 0752
(With that exact spacing)

Ideally when people looking from about 2-3 metres, they know that it is a builder’s business card

Open to suggestions on fonts, layout, style of business card

PLEASE ONLY SUBMIT YOUR BEST OR MAX 3 DESIGNS FOR EACH DESIGNER

Thanks

Industry/Entity Type

Construction. Renovation

Contact Information for Business Card

Details should be the same as the existing card. And addition of what we do.

Requirements
Should not have
• The new business card must not have the same layout as our existing one. Thanks

```html
<!DOCTYPE html>
<html lang="en">
<head>
<meta charset="utf-8">
<title>KeelBuild Business Card</title>
<link href="https://fonts.googleapis.com/css2?family=Noto+Sans:wght@800&family=Poppins:wght@400;600&display=swap" rel="stylesheet">
<style>
  :root {
    --backdrop: #2b2b2b;
    --card-white: #ffffff;
    --card-black: #0b0b0b;
    --ink: #111111;
    --rule: #9a9a9a;
    --pattern-light: #3a3a3a;
    --pattern-dark: #050505;
    --text-light: #f2f2f2;
  }
  * { box-sizing: border-box; margin: 0; padding: 0; }
  html, body {
    width: 1200px; height: 1108px; overflow: hidden;
    background: var(--backdrop);
  }
  .stage {
    position: relative; width: 1200px; height: 1108px;
    display: flex; justify-content: center; align-items: center; gap: 60px;
  }
  .card {
    position: relative; width: 440px; height: 700px;
    border-radius: 26px; overflow: hidden;
    box-shadow: 0 18px 40px rgba(0,0,0,.45);
  }
  /* Front */
  .card--front {
    background: var(--card-white); color: var(--ink);
    display: flex; flex-direction: column; align-items: center;
    font-family: "Poppins", sans-serif;
  }
  .brand {
    margin-top: 150px; display: flex; align-items: center; gap: 12px;
  }
  .brand__mark { width: 18px; height: 18px; background: var(--ink); }
  .brand__name {
    font-family: "Noto Sans", sans-serif; font-weight: 800;
    font-size: 58px; letter-spacing: -0.5px; line-height: 1;
  }
  .person { margin-top: 92px; text-align: center; }
  .person__name {
    font-family: "Noto Sans", sans-serif; font-weight: 800; font-size: 27px;
  }
  .person__role { font-size: 19px; margin-top: -2px; }
  .rule { width: 290px; height: 1px; background: var(--rule); margin: 16px 0 12px; }
  .contact-icons { display: flex; gap: 8px; margin-top: -30px; background: var(--card-white); padding: 0 6px; }
  .contact-icon { width: 30px; height: 30px; background: var(--ink); border-radius: 5px; display: flex; align-items: center; justify-content: center; }
  .contact-list { text-align: center; font-size: 21px; line-height: 1.3; margin-top: 14px; }
  .contact-list__phone { font-weight: 600; font-size: 24px; }
  .social { display: flex; align-items: center; gap: 12px; font-size: 22px; margin-top: 4px; }
  .social__dot { width: 26px; height: 26px; border: 3px solid var(--ink); border-radius: 50%; }
  /* Back */
  .card--back { background: var(--card-black); color: var(--text-light); font-family: "Poppins", sans-serif; }
  .pattern {
    position: absolute; inset: 0;
    background: linear-gradient(200deg, var(--pattern-light) 0%, #1b1b1b 45%, var(--pattern-dark) 80%);
  }
  .back-brand {
    position: absolute; right: 48px; top: 440px;
    display: flex; align-items: center; gap: 8px;
  }
  .back-brand__mark { width: 10px; height: 10px; background: var(--text-light); }
  .back-brand__name { font-family: "Noto Sans", sans-serif; font-weight: 800; font-size: 26px; }
  .services {
    position: absolute; left: 40px; right: 30px; bottom: 74px;
    display: grid; grid-template-columns: repeat(3, auto); column-gap: 14px; row-gap: 2px;
    font-size: 19px; justify-content: start;
  }
  .services li { list-style: none; white-space: nowrap; }
  .services li::before { content: "• "; }
</style>
</head>
<body>
<main class="stage">
  <section class="card card--front">
    <div class="brand">
      <span class="brand__mark"></span>
      <span class="brand__name">KeelBuild</span>
    </div>
    <div class="person">
      <p class="person__name">Daniel Marsh</p>
      <p class="person__role">Residential Builder</p>
    </div>
    <div class="rule"></div>
    <div class="contact-icons">
      <span class="contact-icon">
        <svg width="18" height="18" viewBox="0 0 24 24"><path fill="#fff" d="M6.6 10.8a15 15 0 0 0 6.6 6.6l2.2-2.2c.3-.3.7-.4 1-.2 1.1.4 2.3.6 3.6.6.6 0 1 .4 1 1V20c0 .6-.4 1-1 1A17 17 0 0 1 3 4c0-.6.4-1 1-1h3.5c.6 0 1 .4 1 1 0 1.3.2 2.5.6 3.6.1.3 0 .7-.2 1z"/></svg>
      </span>
      <span class="contact-icon">
        <svg width="18" height="18" viewBox="0 0 24 24"><rect x="2" y="5" width="20" height="14" fill="none" stroke="#fff" stroke-width="2"/><path d="M2 5l10 8 10-8" fill="none" stroke="#fff" stroke-width="2"/></svg>
      </span>
      <span class="contact-icon">
        <svg width="18" height="18" viewBox="0 0 24 24"><circle cx="12" cy="12" r="9" fill="none" stroke="#fff" stroke-width="2"/><path d="M3 12h18M12 3c3 3 3 15 0 18M12 3c-3 3-3 15 0 18" fill="none" stroke="#fff" stroke-width="1.6"/></svg>
      </span>
    </div>
    <div class="contact-list">
      <p class="contact-list__phone">021 0483 0752</p>
      <p>KeelBuild@mailbox.nz</p>
      <p>www.KeelBuild.nz</p>
    </div>
    <div class="rule"></div>
    <div class="social">
      <span class="social__dot"></span>
      <span>KeelBuild.nz</span>
    </div>
  </section>

  <section class="card card--back">
    <div class="pattern" role="img" aria-label="Repeating glossy brand-mark pattern on black"></div>
    <div class="back-brand">
      <span class="back-brand__mark"></span>
      <span class="back-brand__name">KeelBuild</span>
    </div>
    <ul class="services">
      <li>Renovation</li>
      <li>Alteration</li>
      <li>Bathroom</li>
      <li>New Build</li>
      <li>Extension</li>
      <li>Maintenance</li>
    </ul>
  </section>
</main>
</body>
</html>
```